Webdesign für Malerbetrieb
Zielgruppe
Malerbetrieb
Zielgruppe: private Haushalte, Wohnungsverwaltungen
Aufgabenstellung
Das Logo bitte integrieren.
Die Seite darf auf meine potentielle Kunden freundlich und einladend wirken. Die Grundfarben des Logos sollen bitte dezent vertreten werden, die Farbharmonie dabei sollte stimmen.
Da ich kein eigenes Bildmaterial habe, sind natürlich themabezogene Stock-Bilder erwünscht, aber wenn möglich bitte ohne Personen und die Seite nicht mit großen XXL-Bildern überladen.
Ansonsten lasse ich mich gerne von eurer Kreativität überraschen!

```html
<!DOCTYPE html>
<html lang="de">
<head>
<meta charset="utf-8">
<title>Malereibetrieb Lutz – Webdesign</title>
<link href="https://fonts.googleapis.com/css2?family=Open+Sans:wght@300;400;600;700;800&display=swap" rel="stylesheet">
<style>
:root{
  --ink:#2a2d33;
  --text:#444;
  --muted:#888;
  --light:#efeff0;
  --cyan:#1ea0e6;
  --magenta:#d4148c;
  --yellow:#ffe600;
  --white:#fff;
}
*{margin:0;padding:0;box-sizing:border-box}
html,body{width:972px;height:1200px;overflow:hidden;background:var(--white);font-family:"Open Sans",Arial,sans-serif;color:var(--text)}
.page{position:absolute;top:53px;width:400px;background:var(--white);box-shadow:0 4px 18px rgba(0,0,0,.18);overflow:hidden}
.page--home{left:63px;height:1067px}
.page--services{left:508px;height:844px}
.abs{position:absolute}
.topbar{left:0;top:0;width:400px;height:13px;background:var(--ink);color:var(--white);font-size:5px;display:flex;align-items:center;justify-content:space-between;padding:0 14px;font-weight:700}
.topbar .contact{display:flex;gap:10px;font-weight:400}
.topbar .ic{display:inline-block;width:3px;height:3px;background:var(--magenta);margin-right:2px;vertical-align:middle}
.nav{left:0;top:13px;width:400px;height:32px;display:flex;align-items:center;padding:0 14px}
.brand{font-weight:800;font-size:8px;color:var(--ink);letter-spacing:.2px;display:flex;align-items:center;gap:3px;width:100px}
.brand .dot{width:5px;height:5px;background:var(--magenta)}
.menu{display:flex;gap:11px;font-size:4.3px;font-weight:700;color:var(--ink)}
.menu .active{color:var(--magenta)}
.btn{background:var(--ink);color:var(--white);font-size:4.3px;font-weight:700;display:flex;align-items:center;justify-content:center;text-transform:uppercase}
.nav .btn{margin-left:auto;width:35px;height:12px}
.photo{display:block}
.band{left:0;width:400px}
.band--cyan{background:var(--cyan)}
.band--yellow{background:var(--yellow)}
.band--magenta{background:var(--magenta)}
.hero-box{background:rgba(42,45,51,.92);padding:8px 8px}
.hero-title{font-weight:800;color:var(--white);line-height:1}
.hero-sub{font-weight:400;line-height:1.1}
.c-y{color:var(--yellow)}.c-c{color:var(--cyan)}.c-m{color:var(--magenta)}
.section-title{width:400px;text-align:center;font-weight:300;color:var(--ink);line-height:1.05}
.rule{height:1px;background:var(--yellow)}
.small{font-size:4.4px;line-height:1.55}
.center{text-align:center}
.card{width:67px;height:104px;background:var(--light);border:1.2px solid;text-align:center;padding:9px 8px 0}
.card svg{width:18px;height:18px;stroke:var(--ink);fill:none;stroke-width:1}
.card h3{font-size:7px;font-weight:800;color:var(--ink);line-height:1;margin:4px 0 5px}
.card p{font-size:4.1px;line-height:1.6;color:var(--muted)}
.fact{left:200px;width:160px}
.fact h4{font-size:6.5px;font-weight:600;color:var(--ink)}
.fact p{font-size:4.3px;line-height:1.5;margin:5px 0 0 19px}
.fact .btn{width:55px;height:11px;margin:6px 0 0 auto}
.fact svg{position:absolute;left:0;top:-2px;width:14px;height:14px;stroke:var(--ink);fill:none;stroke-width:.8}
.fact .head{padding-left:19px}
.footer{left:0;width:400px;background:var(--ink);color:var(--white)}
.footer .brand{color:var(--white);font-size:10px;width:auto}
.footer .line{height:.6px;background:#777}
.footer .cols{display:flex;font-size:4.3px;line-height:1.8}
.footer .cols div{flex:1}
.footer .legal{display:flex;font-size:4px;font-weight:700}
.tile{width:152px;height:83px;display:flex;flex-direction:column;align-items:center;justify-content:center;color:var(--white);text-align:center}
.tile h3{font-size:7.4px;font-weight:800;line-height:1;text-shadow:0 1px 2px rgba(0,0,0,.25);padding:0 10px}
.tile span{font-size:3.6px;font-weight:600;margin-top:4px}
.tile--info{background:#f3f3f4;color:var(--text);align-items:flex-start;justify-content:flex-start;text-align:left;padding:9px 10px}
.tile--info h3{font-size:5px;font-weight:400;color:var(--ink);text-shadow:none;padding:0}
.tile--info h5{font-size:3.6px;font-weight:700;color:var(--ink);margin-top:2px}
.tile--info i{display:block;width:28px;height:.8px;background:var(--cyan);margin:6px 0 7px}
.tile--info p{font-size:3.7px;line-height:1.5;margin-bottom:4px}
</style>
</head>
<body>

<section class="page page--home">
  <div class="abs topbar"><span>Ihr Malermeister in Kiel</span><span class="contact"><span><i class="ic"></i>0 170 / 5 214 380</span><span><i class="ic"></i>info@malereibetrieb-lutz.de</span></span></div>
  <nav class="abs nav">
    <div class="brand"><span class="dot"></span>Malereibetrieb Lutz</div>
    <div class="menu" style="margin-left:26px"><span>UNSERE LEISTUNGEN</span><span>ÜBER UNS</span><span>WUSSTEN SIE SCHON?</span></div>
    <div class="btn">Kontakt</div>
  </nav>

  <div class="abs photo" role="img" aria-label="Schlafzimmer mit grauem Bett, bunten Kissen, Kugelleuchte und dunkel gestrichener Wand" style="left:0;top:45px;width:400px;height:162px;background:linear-gradient(90deg,#e8e8e8 0%,#cfcfcf 30%,#2b2b2d 50%,#3a3a3c 80%,#5a5a5a 100%)"></div>
  <div class="abs" style="left:0;top:200px;width:400px;height:11px;background:#7a7a7a;clip-path:polygon(0 60%,100% 0,100% 100%,0 100%)"></div>
  <div class="abs hero-box" style="left:42px;top:91px;width:158px;height:41px">
    <div class="hero-title" style="font-size:15px">QUALITÄT</div>
    <div class="hero-sub" style="font-size:8.5px"><span class="c-y">IST</span> <span class="c-c">UNSERE</span> <span class="c-m">LIEBLINGSFARBE</span></div>
  </div>

  <div class="abs" style="left:0;top:211px;width:252px;height:207px;background:var(--light)"></div>
  <div class="abs" style="left:28px;top:248px;width:162px">
    <div style="font-size:8px;font-weight:300;color:var(--ink);line-height:1">HERZLICH WILLKOMMEN</div>
    <div style="font-size:8px;font-weight:800;color:var(--ink);line-height:1.1">BEI MALEREIBETRIEB LUTZ</div>
    <div style="font-size:4.8px;color:var(--muted);margin-top:5px;line-height:1.2">DER MALERMEISTER IHRES VERTRAUENS IN KIEL UND UMGEBUNG</div>
    <div style="height:.6px;background:#bbb;margin:10px 0 12px"></div>
    <p class="small">Bei uns sind Sie genau richtig, wenn Sie Wert auf professionelle, qualitative Leistung legen!</p>
    <p class="small" style="margin-top:3px">Wir sorgen dafür, dass die Decken- und Wandoberflächen glatt gespachtelt, ansatzlos gestrichen oder professionell tapeziert werden. Außerdem erhalten wir Werte, indem wir ansprechend renovieren und neugestalten.</p>
    <p class="small" style="margin-top:3px">Pünktlichkeit, Freundlichkeit, saubere Arbeit und Gewissenhaftigkeit sind bei unserer Arbeit maßgebende Grundsätze, die wir stets einhalten.</p>
    <p class="small" style="margin-top:5px;font-weight:700;color:var(--ink)">Überzeugen Sie sich selbst!</p>
  </div>
  <div class="abs photo" role="img" aria-label="Wohnzimmer mit grauer Wand, braunem Ledersofa, Sessel und Wandspiegel" style="left:200px;top:248px;width:172px;height:126px;background:linear-gradient(180deg,#cfcfd1 0%,#c4c4c6 55%,#8a5a3c 70%,#d8c2a2 100%)"></div>

  <div class="abs band band--cyan" style="top:411px;height:10px;clip-path:polygon(0 50%,100% 0,100% 55%,0 100%)"></div>

  <div class="abs section-title" style="top:458px;font-size:8px">UNSERE<br>LEISTUNGEN</div>
  <div class="abs rule" style="left:98px;top:485px;width:205px"></div>
  <div class="abs center" style="left:40px;top:495px;width:320px;color:var(--ink)">
    <p style="font-size:4.6px;font-weight:700">Werte erhalten-Neues gestalten!</p>
    <p class="small" style="margin-top:3px">Wir verschönern nicht nur, wir schützen und erhalten.</p>
    <p class="small" style="margin-top:3px">Mit unserem fundierten Fachwissen und der richtigen Materialauswahl für Wände und Böden helfen wir Ihnen, den Wert Ihrer Immobilie über viele Jahre zu schützen, zu erhöhen und zu erhalten.</p>
  </div>

  <div class="abs card" style="left:48px;top:541px;border-color:var(--cyan)">
    <svg viewBox="0 0 20 20"><rect x="3" y="2" width="12" height="5" rx="1"/><path d="M15 4h2v5h-7v3"/><rect x="9" y="12" width="2" height="6"/></svg>
    <h3>MALER-<br>ARBEITEN</h3><p>Lorem ipsum dolor sit amet, consectetur adipiscing elit. Ut elit tellus, luctus nec ullamcorper mattis, pulvinar dapibus leo.</p>
  </div>
  <div class="abs card" style="left:127px;top:541px;border-color:var(--yellow)">
    <svg viewBox="0 0 20 20"><rect x="3" y="3" width="14" height="13"/><path d="M6 7h8M6 10h3"/><circle cx="12" cy="12" r="2"/></svg>
    <h3>TAPEZIER-<br>ARBEITEN</h3><p>Lorem ipsum dolor sit amet, consectetur adipiscing elit. Ut elit tellus, luctus nec ullamcorper mattis, pulvinar dapibus leo.</p>
  </div>
  <div class="abs card" style="left:206px;top:541px;border-color:var(--magenta)">
    <svg viewBox="0 0 20 20"><path d="M4 17V4l6 3 4-3 2 5-4 3z"/><path d="M4 17h12"/><path d="M7 13h7"/></svg>
    <h3>LACKIER-<br>ARBEITEN</h3><p>Lorem ipsum dolor sit amet, consectetur adipiscing elit. Ut elit tellus, luctus nec ullamcorper mattis, pulvinar dapibus leo.</p>
  </div>
  <div class="abs card" style="left:285px;top:541px;border-color:#777">
    <svg viewBox="0 0 20 20"><rect x="3" y="3" width="14" height="14"/><path d="M3 10l7-7M3 17L17 3M10 17l7-7M3 3l14 14M3 10l7 7M10 3l7 7"/></svg>
    <h3>BODENBELAGS-<br>ARBEITEN</h3><p>Lorem ipsum dolor sit amet, consectetur adipiscing elit. Ut elit tellus, luctus nec ullamcorper mattis, pulvinar dapibus leo.</p>
  </div>
  <div class="abs btn" style="left:161px;top:672px;width:79px;height:12px">Alle Leistungen im Detail →</div>

  <div class="abs band band--yellow" style="top:718px;height:10px;clip-path:polygon(0 55%,100% 0,100% 50%,0 100%)"></div>

  <div class="abs" style="left:0;top:728px;width:148px;height:225px;background:var(--light)"></div>
  <div class="abs photo" role="img" aria-label="Farbeimer in Anthrazit mit weißem Deckel" style="left:86px;top:782px;width:96px;height:112px;border-radius:45% 45% 40% 40%;background:linear-gradient(160deg,#f4f4f4 0%,#d6d6d6 25%,#4a4c52 45%,#2c2e33 100%)"></div>
  <div class="abs" style="left:200px;top:767px;width:160px">
    <div style="font-size:8px;font-weight:300;color:var(--ink);line-height:1.05">WUSSTEN<br>SIE SCHON?</div>
    <div style="height:.6px;background:var(--magenta);margin-top:8px"></div>
  </div>
  <div class="abs fact" style="top:806px">
    <svg viewBox="0 0 14 14"><ellipse cx="7" cy="8" rx="5" ry="3.5"/><path d="M4 11v2M10 11v2M6 4h2"/></svg>
    <h4 class="head">STEUERVORTEILE</h4>
    <p>Steuervorteil für Privatleute für handwerkliche Tätigkeiten? Sie können 20% der Rechnung vom Finanzamt ersetzt bekommen.</p>
    <div class="btn">Mehr erfahren →</div>
    <div style="height:.6px;background:var(--cyan);margin-top:10px"></div>
  </div>
  <div class="abs fact" style="top:871px">
    <svg viewBox="0 0 14 14"><circle cx="7" cy="7" r="3.5"/><circle cx="2" cy="3" r="1"/><circle cx="12" cy="3" r="1"/><circle cx="2" cy="11" r="1"/><circle cx="12" cy="11" r="1"/></svg>
    <h4 class="head">SCHIMMEL IM WOHNRAUM</h4>
    <p>Schimmel kann Ihre Gesundheit beeinträchtigen. Was sie dagegen tun können, erfahren Sie hier.</p>
    <div class="btn">Mehr erfahren →</div>
  </div>

  <div class="abs band band--magenta" style="top:951px;height:9px;clip-path:polygon(0 55%,100% 0,100% 100%,0 100%)"></div>
  <footer class="abs footer" style="top:959px;height:108px;padding:18px 42px 0">
    <div class="brand"><span class="dot"></span>Malereibetrieb Lutz</div>
    <div class="line" style="margin:14px 0 5px"></div>
    <div class="cols"><div>Lindenweg 14 b<br>24103 Kiel</div><div>0 170 / 5 214 380<br>0 123 / 456 789 0</div><div>info@malereibetrieb-lutz.de<br>www.malereibetrieb-lutz.de</div></div>
    <div class="line" style="margin:5px 0 8px"></div>
    <div class="legal"><span style="width:207px">©2020 MALEREIBETRIEB LUTZ | Alle Rechte vorbehalten</span><span style="margin-right:11px">IMPRESSUM</span><span>DATENSCHUTZ</span></div>
  </footer>
</section>

<section class="page page--services">
  <div class="abs topbar"><span>Ihr Malermeister in Kiel</span><span class="contact"><span><i class="ic"></i>0 170 / 5 214 380</span><span><i class="ic"></i>info@malereibetrieb-lutz.de</span></span></div>
  <nav class="abs nav">
    <div class="brand"><span class="dot"></span>Malereibetrieb Lutz</div>
    <div class="menu" style="margin-left:26px"><span class="active">UNSERE LEISTUNGEN</span><span>ÜBER UNS</span><span>WUSSTEN SIE SCHON?</span></div>
    <div class="btn">Kontakt</div>
  </nav>
  <div class="abs photo" role="img" aria-label="Wohnraum mit grauem Sofa, Couchtisch und Holzboden vor blaugrauer Wand" style="left:0;top:45px;width:400px;height:90px;background:linear-gradient(180deg,#596c78 0%,#6d7f8a 60%,#8a8c8e 100%)"></div>
  <div class="abs band band--cyan" style="top:127px;height:11px;clip-path:polygon(0 45%,100% 0,100% 100%,0 100%)"></div>
  <div class="abs" style="left:28px;top:77px">
    <div class="hero-title" style="font-size:15px">IHRE ZUFRIEDENHEIT</div>
    <div class="hero-sub" style="font-size:8.5px"><span class="c-y">IST</span> <span class="c-c">UNSER</span> <span class="c-m">ANSPRUCH</span></div>
  </div>

  <div class="abs section-title" style="top:175px;font-size:9px">UNSERE LEISTUNGEN</div>
  <div class="abs rule" style="left:98px;top:193px;width:205px"></div>
  <div class="abs center" style="left:40px;top:203px;width:320px">
    <p style="font-size:4.6px;font-weight:600;color:var(--ink)">Wir bieten klassische Malerarbeiten wie Tapezierarbeiten, Lackierarbeiten und Bodenbelagsarbeiten</p>
    <p class="small" style="margin-top:5px">Spachteln, Streichen, Lackieren und Tapezieren gehören zu unserem täglichen Geschäft als Maler und auch das Gestalten von Wänden mit hochwertigen Maltechniken, wie zum Beispiel Lasur- und Spachteltechniken.</p>
  </div>

  <div class="abs tile" role="img" aria-label="Sessel und Beistelltisch vor petrolfarbener Wand" style="left:45px;top:236px;background:linear-gradient(180deg,#6f8c92,#8fa3a5)"><h3>FARBLICHE DECKEN- UND WANDGESTALTUNG</h3><span>BERÜHREN UM MEHR ZU ERFAHREN &gt;&gt;</span></div>
  <div class="abs tile tile--info" style="left:203px;top:236px">
    <h3>TAPEZIERARBEITEN</h3><h5>GEBEN SIE IHREN WÄNDEN DAS GEWISSE EXTRA</h5><i></i>
    <p>Ein Raum wird erst dann zu einer Wohlfühl-Oase, wenn der Charakter des Raumes hervorgehoben wird. Dies können wir nicht nur mit klassischen Tapeten wie Raufaser oder Glattvlies, sondern manchmal lohnt sich auch der Griff zu effektvolleren Tapeten.</p>
    <p>Wir beraten Sie gerne zu den verschiedenen Möglichkeiten und finden gemeinsam die ideale Ergänzung zu Ihrem Raumkonzept.</p>
  </div>
  <div class="abs tile" role="img" aria-label="Heizkörper an grauer Wand über Holzboden" style="left:45px;top:325px;background:linear-gradient(180deg,#9a9a9c,#6c6463)"><h3>LACKIER- &amp; LASURARBEITEN</h3><span>BERÜHREN UM MEHR ZU ERFAHREN &gt;&gt;</span></div>
  <div class="abs tile" role="img" aria-label="Umzugskartons in hellem Raum" style="left:203px;top:325px;background:linear-gradient(180deg,#b9b4ad,#a08a70)"><h3>PREISWERTE ÜBERGABERENOVIERUNGEN</h3><span>BERÜHREN UM MEHR ZU ERFAHREN &gt;&gt;</span></div>
  <div class="abs tile" role="img" aria-label="Spachtel an heller Wand" style="left:45px;top:414px;background:linear-gradient(180deg,#b8b8b8,#a6a6a6)"><h3>SPACHTELARBEITEN</h3><span>BERÜHREN UM MEHR ZU ERFAHREN &gt;&gt;</span></div>
  <div class="abs tile" role="img" aria-label="Weiße Hausfassade mit Betonfläche" style="left:203px;top:414px;background:linear-gradient(180deg,#a9adb2,#8e9397)"><h3>FASSADENANSTRICHE</h3><span>BERÜHREN UM MEHR ZU ERFAHREN &gt;&gt;</span></div>
  <div class="abs tile" role="img" aria-label="Farbspritzpistole vor grauer Wand" style="left:45px;top:503px;background:linear-gradient(180deg,#8f8f90,#7a7a7b)"><h3>AIRLESS (SPRITZVERFAHREN)</h3><span>BERÜHREN UM MEHR ZU ERFAHREN &gt;&gt;</span></div>
  <div class="abs tile" role="img" aria-label="Farbeimer mit grüner Farbe und Malerwerkzeug" style="left:203px;top:503px;background:linear-gradient(135deg,#6d86a8,#9fb0c0 60%,#b7b84a)"><h3>MODERNE &amp; TRADITIONELLE TECHNIKEN</h3><span>BERÜHREN UM MEHR ZU ERFAHREN &gt;&gt;</span></div>
  <div class="abs tile" role="img" aria-label="Küche mit Holzbalken unter Dachschräge" style="left:45px;top:592px;background:linear-gradient(180deg,#8a7a6c,#b59a7a)"><h3>HOLZSCHUTZ</h3><span>BERÜHREN UM MEHR ZU ERFAHREN &gt;&gt;</span></div>
  <div class="abs tile" role="img" aria-label="Badezimmer mit Holzboden und freistehender Wanne" style="left:203px;top:592px;background:linear-gradient(180deg,#5e5e60,#7d6a55)"><h3>BODENBELAGSARBEITEN</h3><span>BERÜHREN UM MEHR ZU ERFAHREN &gt;&gt;</span></div>

  <div class="abs band band--magenta" style="top:727px;height:10px;clip-path:polygon(0 55%,100% 0,100% 100%,0 100%)"></div>
  <footer class="abs footer" style="top:736px;height:108px;padding:18px 42px 0">
    <div class="brand"><span class="dot"></span>Malereibetrieb Lutz</div>
    <div class="line" style="margin:14px 0 5px"></div>
    <div class="cols"><div>Lindenweg 14 b<br>24103 Kiel</div><div>0 170 / 5 214 380<br>0 123 / 456 789 0</div><div>info@malereibetrieb-lutz.de<br>www.malereibetrieb-lutz.de</div></div>
    <div class="line" style="margin:5px 0 8px"></div>
    <div class="legal"><span style="width:207px">©2020 MALEREIBETRIEB LUTZ | Alle Rechte vorbehalten</span><span style="margin-right:11px">IMPRESSUM</span><span>DATENSCHUTZ</span></div>
  </footer>
</section>

</body>
</html>
```